Business Card Design

I need a business card design for a new company based in Sydney called 'The Copper Ladle'. We deliver organic, gourmet and fine foods to your door.

I would like to see creative, unique designs which use colours which represent health and nature like green.

Target Market(s)

Health conscious 20 to 35 year olds.

Industry/Entity Type

Health

Contact Information for Business Card

The Copper Ladle, Owen Barclett, owen@thecopperladle.com.au, 0427685392

Requirements
Must have
• My logo.

```html
<!DOCTYPE html>
<html lang="en">
<head>
<meta charset="utf-8">
<title>The Copper Ladle — Business Card</title>
<link rel="stylesheet" href="https://fonts.googleapis.com/css2?family=Josefin+Sans:wght@300;400&family=Open+Sans:wght@400;700&display=swap">
<style>
  :root {
    --page: #ffffff;
    --brand-green: #3f9a1c;
    --name-green: #2f8a1f;
    --icon-green: #8ed42a;
    --ink: #333333;
    --card-edge: #a8a8a8;
    --wash-green: #eaf6dc;
    --ghost-light: #f6f6f6;
    --ghost-mid: #e9e9e9;
  }
  * { box-sizing: border-box; margin: 0; padding: 0; }
  html, body {
    width: 989px;
    height: 1200px;
    overflow: hidden;
    background: var(--page);
  }
  .sheet {
    position: relative;
    width: 989px;
    height: 1200px;
  }

  /* Front face */
  .card-front {
    position: absolute;
    left: 77px;
    top: 77px;
    width: 822px;
    height: 451px;
    background: linear-gradient(to bottom, #ffffff 0%, #fbfdf8 55%, var(--wash-green) 100%);
  }
  .brand {
    position: absolute;
    left: 160px;
    top: 150px;
    display: flex;
    align-items: center;
    gap: 22px;
  }
  .brand-dot {
    width: 150px;
    height: 150px;
    border-radius: 50%;
    background: var(--icon-green);
    flex: none;
  }
  .brand-name {
    font-family: "Josefin Sans", sans-serif;
    font-weight: 300;
    font-size: 70px;
    line-height: 0.95;
    color: var(--brand-green);
    letter-spacing: 0.5px;
  }

  /* Back face */
  .card-back {
    position: absolute;
    left: 75px;
    top: 607px;
    width: 834px;
    height: 508px;
    background: var(--page);
    border: 1px solid var(--card-edge);
    overflow: hidden;
  }
  .emblem-ghost {
    position: absolute;
    left: 0;
    top: 0;
    width: 380px;
    height: 508px;
    background: linear-gradient(100deg, var(--ghost-mid) 0%, var(--ghost-light) 70%, #ffffff 100%);
    border-radius: 0 60% 45% 0 / 0 40% 45% 0;
  }
  .contact {
    position: absolute;
    right: 64px;
    top: 150px;
    text-align: right;
  }
  .contact-name {
    font-family: "Josefin Sans", sans-serif;
    font-weight: 400;
    font-size: 50px;
    line-height: 1;
    color: var(--name-green);
  }
  .contact-email {
    margin-top: 12px;
    font-family: "Open Sans", sans-serif;
    font-size: 25px;
    color: var(--ink);
  }
  .contact-phone {
    margin-top: 44px;
    display: inline-flex;
    align-items: center;
    gap: 16px;
    font-family: "Open Sans", sans-serif;
    font-weight: 700;
    font-size: 33px;
    color: var(--ink);
  }
  .phone-icon { width: 42px; height: 42px; flex: none; }
</style>
</head>
<body>
<main class="sheet">

  <section class="card-front" aria-label="Card front">
    <div class="brand">
      <span class="brand-dot"></span>
      <span class="brand-name">The Copper<br>Ladle</span>
    </div>
  </section>

  <section class="card-back" aria-label="Card back">
    <div class="emblem-ghost" role="img" aria-label="Faint oversized brand emblem in pale grey"></div>
    <div class="contact">
      <p class="contact-name">Owen Barclett</p>
      <p class="contact-email">owen@thecopperladle.com.au</p>
      <p class="contact-phone">
        <svg class="phone-icon" viewBox="0 0 42 42" aria-hidden="true">
          <circle cx="21" cy="21" r="19" fill="none" stroke="var(--icon-green)" stroke-width="2.5"/>
          <path d="M16 11c-2 1-4 3-3 7 1 5 5 11 10 13 3 1 5 0 6-2l-4-4-2 2c-2-1-5-5-6-7l2-2z" fill="var(--icon-green)"/>
        </svg>
        <span>0427 685 392</span>
      </p>
    </div>
  </section>

</main>
</body>
</html>
```